Life Saving Rules KDBRX

Design a wallet/business card size document front and back to depict the attached lifesaving rules in the color scheme of the business logo attached. (Also attached is an example of a similar card)

Target Market(s)

End User - Field Employees

Industry/Entity Type

Refining

Requirements
Must have
• All Life Saving rules with graphics, using front and back of card, information needs to flow.
Nice to have
• Would like the design to be similar to the card uploaded but better with graphics

```html
<!DOCTYPE html>
<html lang="en">
<head>
<meta charset="utf-8">
<title>KDBRX Life Saving Rules – Wallet Card</title>
<link rel="stylesheet" href="https://fonts.googleapis.com/css2?family=Poppins:wght@300;400;500;600;700&display=swap">
<style>
  :root {
    --board: #58595b;
    --card: #ffffff;
    --blue: #00a4e0;
    --green: #76bc43;
    --ink: #4a4a4c;
    --ink-dark: #3a3a3c;
    --icon-grey: #e6e7e8;
    --icon-green: #e4f1da;
  }
  * { box-sizing: border-box; margin: 0; padding: 0; }
  html, body {
    width: 915px; height: 1200px; overflow: hidden;
    background: var(--board);
    font-family: "Poppins", sans-serif;
  }
  .card {
    position: absolute; left: 117px; width: 681px; height: 389px;
    background: var(--card);
    box-shadow: 0 6px 14px rgba(0,0,0,.35);
    overflow: hidden;
  }
  .card--front { top: 123px; }
  .card--back { top: 648px; }
  .card__band { position: absolute; left: 0; top: 0; width: 681px; height: 36px; }
  .brand {
    position: absolute; left: 30px; top: 86px;
    display: flex; align-items: center; gap: 10px;
    font-weight: 600; font-size: 30px; color: var(--ink); letter-spacing: .5px;
  }
  .brand__mark { width: 18px; height: 18px; background: var(--green); }
  .title { position: absolute; left: 297px; top: 30px; line-height: 1; }
  .title__top {
    font-weight: 300; font-size: 46px; letter-spacing: 9px; color: var(--ink);
  }
  .title__main {
    margin-top: 2px; font-weight: 700; font-size: 46px; color: var(--ink-dark);
    letter-spacing: .5px;
  }
  .title__main .accent { color: var(--green); }
  .rule {
    position: absolute; text-align: center;
    transform: translateX(-50%);
  }
  .rule__icon { width: 64px; height: 62px; margin: 0 auto; border-radius: 4px; }
  .rule__icon--grey { background: var(--icon-grey); }
  .rule__icon--green { background: var(--icon-green); }
  .rule__name { font-weight: 700; font-size: 15px; line-height: 17px; }
  .card--front .rule { top: 160px; width: 150px; }
  .card--front .rule__name { color: var(--blue); margin-top: 11px; }
  .card--back .rule { top: 169px; width: 150px; }
  .card--back .rule__icon { height: 68px; }
  .card--back .rule__name { color: var(--ink); margin-top: 9px; font-weight: 600; font-size: 15.5px; }
  .rule__text {
    font-weight: 500; font-size: 12px; line-height: 14px; color: var(--ink-dark);
    margin-top: 8px;
  }
  .divider {
    position: absolute; width: 0; border-left: 1.3px dashed var(--ink-dark);
  }
  .card--front .divider { top: 160px; height: 175px; }
  .card--back .divider { top: 169px; height: 158px; }
</style>
</head>
<body>

<section class="card card--front" aria-label="Life saving rules, front">
  <svg class="card__band" viewBox="0 0 681 36" aria-hidden="true">
    <polygon points="0,0 681,0 681,36 502,36 487,9 0,9" fill="var(--blue)"/>
    <polygon points="489,0 681,0 681,29 504,29" fill="var(--green)"/>
  </svg>
  <div class="brand"><span class="brand__mark"></span>KDBRX</div>
  <h1 class="title">
    <div class="title__top">LIFE</div>
    <div class="title__main"><span class="accent">SAVING</span> RULES</div>
  </h1>

  <div class="rule" style="left:96px">
    <div class="rule__icon rule__icon--grey" role="img" aria-label="Icon: worker asking supervisor for authorization at a safety control"></div>
    <h2 class="rule__name">Bypassing Safety<br>Controls</h2>
    <p class="rule__text">Obtain authorization<br>before overriding<br>or disabling<br>safety controls</p>
  </div>
  <div class="divider" style="left:185px"></div>

  <div class="rule" style="left:262px">
    <div class="rule__icon rule__icon--grey" role="img" aria-label="Icon: worker beside an open door"></div>
    <h2 class="rule__name">Confined<br>Space</h2>
    <p class="rule__text">Confined Space<br>Obtain authorization<br>before entering a<br>confined space</p>
  </div>
  <div class="divider" style="left:353px"></div>

  <div class="rule" style="left:428px">
    <div class="rule__icon rule__icon--grey" role="img" aria-label="Icon: lightning bolt, padlock and empty battery"></div>
    <h2 class="rule__name">Energy<br>Isolation</h2>
    <p class="rule__text">Verify isolation<br>and zero energy<br>before work begins</p>
  </div>
  <div class="divider" style="left:514px"></div>

  <div class="rule" style="left:589px">
    <div class="rule__icon rule__icon--green" role="img" aria-label="Icon: flame"></div>
    <h2 class="rule__name">Hot<br>Work</h2>
    <p class="rule__text">Control<br>flammables<br>and ignition<br>sources</p>
  </div>
</section>

<section class="card card--back" aria-label="Life saving rules, back">
  <svg class="card__band" viewBox="0 0 681 36" aria-hidden="true">
    <polygon points="0,0 681,0 681,36 502,36 487,9 0,9" fill="var(--blue)"/>
    <polygon points="489,0 681,0 681,29 504,29" fill="var(--green)"/>
  </svg>
  <div class="brand"><span class="brand__mark"></span>KDBRX</div>
  <h1 class="title">
    <div class="title__top">LIFE</div>
    <div class="title__main"><span class="accent">SAVING</span> RULES</div>
  </h1>

  <div class="rule" style="left:168px">
    <div class="rule__icon rule__icon--grey" role="img" aria-label="Icon: crane lifting a load"></div>
    <h2 class="rule__name">Safe Mechanical<br>Lifting</h2>
    <p class="rule__text">Plan lifting<br>operations &amp;<br>control the area</p>
  </div>
  <div class="divider" style="left:260px"></div>

  <div class="rule" style="left:351px">
    <div class="rule__icon rule__icon--grey" role="img" aria-label="Icon: clipboard with checklist"></div>
    <h2 class="rule__name">Work<br>Authorization</h2>
    <p class="rule__text">Work with a<br>valid permit<br>when required</p>
  </div>
  <div class="divider" style="left:441px"></div>

  <div class="rule" style="left:530px">
    <div class="rule__icon rule__icon--grey" role="img" aria-label="Icon: worker falling while tied to a lanyard"></div>
    <h2 class="rule__name">Fall<br>Protection</h2>
    <p class="rule__text">Protect yourself<br>against fall when<br>working at height</p>
  </div>
</section>

</body>
</html>
```